Business Cards

I'd like help creating business cards with the full logo "Veltrona Capital Partners" on the back of the card (navy background with white writing), and abbreviated logo "VCP" on the front. Would like to list name, title, phone number, email, and website listed on front of card. Would like to keep very simple. Front font Arial or similar.

```html
<!DOCTYPE html>
<html lang="en">
<head>
<meta charset="utf-8">
<title>Veltrona Capital Partners – Business Cards</title>
<link rel="stylesheet" href="https://fonts.googleapis.com/css2?family=Arimo:wght@400;700&family=Montserrat:wght@700&display=swap">
<style>
  :root {
    --navy: #1f3566;
    --white: #ffffff;
    --paper: #f7f7f7;
    --ink: #333333;
    --rule: #9a9a9a;
    --stage: #e6e2dc;
  }
  * { margin: 0; padding: 0; box-sizing: border-box; }
  html, body { width: 1200px; height: 900px; overflow: hidden; }
  body {
    background: var(--stage);
    position: relative;
    font-family: "Arimo", Arial, sans-serif;
  }
  .card {
    position: absolute;
    left: 280px;
    width: 640px;
    height: 366px;
    border-radius: 26px;
    box-shadow: 0 6px 18px rgba(0,0,0,0.18);
    overflow: hidden;
  }
  .card--back { top: 64px; background: var(--navy); }
  .card--front { top: 470px; background: var(--paper); }

  .wordmark {
    position: absolute;
    inset: 0;
    display: flex;
    align-items: center;
    justify-content: center;
    font-family: "Montserrat", Arial, sans-serif;
    font-weight: 700;
    font-size: 30px;
    letter-spacing: 2px;
    color: var(--white);
    text-transform: uppercase;
  }

  .monogram {
    position: absolute;
    left: 36px;
    top: 40px;
    display: flex;
    align-items: center;
    gap: 14px;
  }
  .monogram__square {
    width: 22px;
    height: 22px;
    background: var(--navy);
  }
  .monogram__name {
    font-family: "Arimo", Arial, sans-serif;
    font-weight: 700;
    font-size: 84px;
    line-height: 1;
    color: var(--navy);
    letter-spacing: 2px;
  }

  .identity {
    position: absolute;
    right: 296px;
    bottom: 60px;
    text-align: right;
  }
  .identity__name {
    font-weight: 700;
    font-size: 22px;
    color: var(--navy);
    letter-spacing: 0.5px;
  }
  .identity__title {
    font-size: 16px;
    color: var(--ink);
    margin-top: 3px;
  }

  .divider {
    position: absolute;
    left: 360px;
    bottom: 46px;
    width: 1px;
    height: 86px;
    background: var(--rule);
  }

  .contacts {
    position: absolute;
    left: 378px;
    bottom: 50px;
    list-style: none;
  }
  .contacts__item {
    display: flex;
    align-items: center;
    gap: 8px;
    font-size: 14px;
    color: var(--ink);
    height: 26px;
  }
  .contacts__icon { width: 15px; height: 15px; flex: none; }
</style>
</head>
<body>

  <section class="card card--back" aria-label="Card back">
    <div class="wordmark">Veltrona Capital Partners</div>
  </section>

  <section class="card card--front" aria-label="Card front">
    <div class="monogram">
      <span class="monogram__square"></span>
      <span class="monogram__name">VCP</span>
    </div>

    <div class="identity">
      <p class="identity__name">DANA CORVELL</p>
      <p class="identity__title">Co-Founder and Managing Partner</p>
    </div>

    <span class="divider"></span>

    <ul class="contacts">
      <li class="contacts__item">
        <svg class="contacts__icon" viewBox="0 0 16 16" aria-hidden="true">
          <path fill="#1f3566" d="M3.2 1.5l2.3 2.6-1.2 1.6c.9 2 2.2 3.3 4.1 4.2l1.6-1.2 2.6 2.3-1.3 2.3C6.6 13.2 2.6 9.3 1 4.3z"/>
        </svg>
        (555) 214-3090
      </li>
      <li class="contacts__item">
        <svg class="contacts__icon" viewBox="0 0 16 16" aria-hidden="true">
          <rect x="1" y="3" width="14" height="10" fill="#1f3566"/>
          <path d="M1.5 3.5L8 9l6.5-5.5" fill="none" stroke="#f7f7f7" stroke-width="1.2"/>
        </svg>
        Dana.Corvell@VeltronaCP.com
      </li>
      <li class="contacts__item">
        <svg class="contacts__icon" viewBox="0 0 16 16" aria-hidden="true">
          <g fill="none" stroke="#1f3566" stroke-width="1.2">
            <circle cx="8" cy="8" r="6.5"/>
            <ellipse cx="8" cy="8" rx="3" ry="6.5"/>
            <path d="M1.5 8h13M2.5 4.8h11M2.5 11.2h11"/>
          </g>
        </svg>
        www.veltronacp.com
      </li>
    </ul>
  </section>

</body>
</html>
```